We need a business card design for a new soccer program based in Melbourne, Victoria, Australia.
Coaching kids from 2 through to 14 develop social, motor and soccer skills, in a fun and friendly non-competitive environment.
Our company colours are blue and orange as seen in the logo attached below. However, we are happy for the font to be any modern colour that looks professional.
Target Market(s)
Mums and dads
Industry/Entity Type
Business
Contact Information for Business Card
business name: Bright Kick Soccer
Marko Delvino Director- 0451 738 015
Luke Ferrano Director- 0419 856 371
Tomas Kovalenko Head Coach
email: marko@brightkicksoccer.com.au
website: www.brightkicksoccer.com.au
Coaching kids from 2-14
https://www.facebook.com/brightkicksoccer (facebook page not required unless it looks good without being clustered)
Look and feel

```html
<!DOCTYPE html>
<html lang="en">
<head>
<meta charset="utf-8">
<title>Bright Kick Soccer – Business Card</title>
<link rel="stylesheet" href="https://fonts.googleapis.com/css2?family=Roboto+Condensed:wght@300;400;700&family=Dancing+Script:wght@500&display=swap">
<style>
  :root {
    --backdrop: #2f8a4e;
    --field-yellow: #e6e62a;
    --field-pale: #f1f08a;
    --grass: #3f8f2c;
    --grass-dark: #2c6a1f;
    --brand-orange: #e27d22;
    --name-green: #1e5b2c;
    --band-light: rgba(120, 118, 80, 0.78);
    --band-mid: rgba(95, 94, 62, 0.85);
    --band-dark: rgba(62, 62, 38, 0.92);
    --tagline: #b6b46c;
    --white: #ffffff;
  }
  * { margin: 0; padding: 0; box-sizing: border-box; }
  html, body {
    width: 1200px; height: 1000px; overflow: hidden;
    background: var(--backdrop);
    font-family: "Roboto Condensed", "Arial Narrow", sans-serif;
  }
  .canvas { position: relative; width: 1200px; height: 1000px; }
  .card {
    position: absolute; width: 780px; height: 460px; overflow: hidden;
    box-shadow: 0 8px 22px rgba(0,0,0,0.3);
  }

  /* Front */
  .card--front { left: 40px; top: 30px; }
  .front__field {
    position: absolute; inset: 0;
    background:
      linear-gradient(160deg, transparent 52%, var(--grass) 53%, var(--grass-dark) 100%),
      linear-gradient(120deg, var(--field-yellow), var(--field-pale) 55%, var(--field-yellow));
  }
  .brand {
    position: absolute; left: 150px; top: 150px;
    display: flex; align-items: center; gap: 22px;
  }
  .brand__dot {
    width: 110px; height: 110px; border-radius: 50%;
    background: var(--white);
  }
  .brand__name {
    font-weight: 700; font-size: 64px; line-height: 1;
    color: var(--brand-orange); text-transform: uppercase;
    width: 380px;
  }

  /* Back */
  .card--back { left: 380px; top: 510px; }
  .back__field {
    position: absolute; inset: 0;
    background:
      linear-gradient(180deg, var(--field-yellow) 0%, var(--field-pale) 20%, var(--field-yellow) 26%, #8e9a3c 40%, #6f7a30 100%);
  }
  .back__name {
    position: absolute; top: 18px; left: 0; right: 0; text-align: center;
    font-family: "Dancing Script", cursive; font-weight: 500;
    font-size: 60px; color: var(--name-green); letter-spacing: 2px;
  }
  .band { position: absolute; left: 0; right: 0; display: flex; align-items: center; justify-content: center; color: var(--white); }
  .band--role { top: 118px; height: 62px; background: var(--band-light); font-size: 42px; font-weight: 300; gap: 12px; }
  .band--role .phone { font-weight: 700; letter-spacing: 1px; }
  .band--email { top: 180px; height: 46px; background: var(--band-mid); font-size: 27px; font-weight: 300; }
  .band--tagline { top: 226px; height: 150px; background: var(--band-dark); color: var(--tagline); font-size: 60px; font-weight: 700; letter-spacing: 1px; }
  .band--web { top: 390px; height: 70px; background: var(--band-mid); font-size: 30px; font-weight: 400; }
</style>
</head>
<body>
<main class="canvas">
  <section class="card card--front" aria-label="Business card front">
    <div class="front__field" role="img" aria-label="Photo of a grass soccer pitch corner with white chalk lines under yellow texture"></div>
    <div class="brand">
      <span class="brand__dot"></span>
      <span class="brand__name">Bright Kick Soccer</span>
    </div>
  </section>

  <section class="card card--back" aria-label="Business card back">
    <div class="back__field" role="img" aria-label="Textured soccer pitch with yellow wash and chalk lines"></div>
    <h1 class="back__name">Marko Delvino</h1>
    <div class="band band--role"><span class="role">Director</span><span class="phone">0451 738 015</span></div>
    <div class="band band--email">marko@brightkicksoccer.com.au</div>
    <div class="band band--tagline">Coaching kids from 2-14</div>
    <div class="band band--web">www.brightkicksoccer.com.au</div>
  </section>
</main>
</body>
</html>
```